HollowPine Ventures Inc. Business Card Design

My business is custom renovations and homes.I would need to have a new business logo created to go along with my company name. The business card should be of a modern style as this is the market I am focused on. I would need my contact information and website posted on the card. I would also like to list a few of the tasks I conduct on the card (such as: Renovations, Additions, Repairs, New Homes, Design, Consultations). On the reverse of the card I currently have just my logo and my motto, "Shaping A Bold Path". However, I am open to completely changing everything as I am starting a new year and would like to excel further. Any new ideas and suggestions are always welcomed. Thank you.

Target Market(s)

Upscale residential and commercial renovations and builds

Industry/Entity Type

Business

Contact Information for Business Card

I would like the design to be able to be laser cut or burnt onto a wooden business card. I will be creating one option of cards for really loyal customers (wooden) and a second option for the everyday customer (paper).

Font styles to use
Other font styles liked:
• Calibri / anything of mordern taste

Colors
f37122
5c5c5c
474747
ffffff

Requirements
Must have
• I would like the colours of my business to be a sharp orange and grey. I believe this will symbolize a modern style. I am open to other suggestions if this is not suitable for the designers tastes. My contact info as follows:
• Will Marsh
• President
• HollowPine Ventures Inc.
• 555-214-3987
• will@hollowpineventures.example
• I would like my website (currently under construction) hollowpineventures.example on the card aswell.
Nice to have
• Along with a modern logo representing HollowPine, I would like something on the card besides the logo and contact information. Perhaps a small background design. I feel it may be nice to have my services listed on the card (in smaller font on the bottom) Renovations, Additions, Repairs, Design, Consultations.
Should not have
• The business card should not have too many different colors. Should not have rounded corners.

```html
<!DOCTYPE html>
<html lang="en">
<head>
<meta charset="utf-8">
<title>HollowPine Ventures Inc. – Business Card</title>
<link rel="stylesheet" href="https://fonts.googleapis.com/css2?family=Roboto:wght@400;500;700&display=swap">
<style>
  :root {
    --orange: #f37122;
    --navy: #1f2b3d;
    --ink: #222222;
    --white: #ffffff;
    --backdrop: #e4e6e8;
  }
  * { margin: 0; padding: 0; box-sizing: border-box; }
  html, body {
    width: 1200px;
    height: 1192px;
    overflow: hidden;
    background: var(--backdrop);
    font-family: "Roboto", Arial, sans-serif;
  }
  .card {
    position: absolute;
    left: 299px;
    width: 741px;
    height: 427px;
    background: var(--white);
    overflow: hidden;
  }
  .card--front { top: 128px; }
  .card--back { top: 640px; }
  .card__shapes { position: absolute; inset: 0; }

  .brand {
    position: absolute;
    text-align: center;
    color: var(--ink);
  }
  .brand__name {
    display: flex;
    align-items: center;
    justify-content: center;
    gap: 10px;
    font-weight: 700;
    color: var(--orange);
    line-height: 1;
  }
  .brand__square { background: var(--orange); flex: none; }
  .brand__legal { font-weight: 500; margin-top: 14px; }

  .card--front .brand { left: 0; width: 260px; top: 150px; }
  .card--front .brand__name { font-size: 34px; }
  .card--front .brand__square { width: 14px; height: 14px; }
  .card--front .brand__legal { font-size: 17px; }

  .card--back .brand { left: 150px; width: 300px; top: 150px; }
  .card--back .brand__name { font-size: 48px; }
  .card--back .brand__square { width: 18px; height: 18px; }
  .card--back .brand__legal { font-size: 19px; margin-top: 18px; }

  .contact {
    position: absolute;
    left: 318px;
    top: 132px;
    width: 390px;
    color: var(--white);
  }
  .contact__name { font-size: 40px; font-weight: 700; line-height: 1.1; }
  .contact__title { font-size: 23px; font-weight: 400; margin-top: 4px; }
  .contact__rule { height: 2px; background: var(--white); width: 280px; margin: 14px 0 26px; opacity: .9; }
  .contact__list { list-style: none; }
  .contact__item {
    display: flex;
    align-items: center;
    gap: 20px;
    font-size: 20px;
    height: 48px;
  }
  .contact__icon { width: 24px; height: 24px; flex: none; }

  .services {
    position: absolute;
    left: 0;
    right: 0;
    top: 360px;
    display: flex;
    justify-content: center;
    gap: 22px;
    list-style: none;
    font-size: 16px;
    font-weight: 500;
    color: var(--ink);
  }
  .services__item { display: flex; align-items: center; gap: 9px; }
  .services__item::before {
    content: "";
    width: 13px;
    height: 13px;
    border-radius: 50%;
    background: var(--ink);
  }
</style>
</head>
<body>

<section class="card card--front" aria-label="Business card front">
  <svg class="card__shapes" viewBox="0 0 741 427" aria-hidden="true">
    <polygon points="267,0 741,0 741,427 267,427" fill="var(--orange)"/>
    <polygon points="250,0 282,0 267,42 267,62 250,62" fill="var(--navy)"/>
    <polygon points="267,365 267,427 285,427" fill="var(--navy)"/>
    <polygon points="246,400 267,365 267,427 246,427" fill="var(--navy)"/>
  </svg>

  <div class="brand">
    <div class="brand__name"><span class="brand__square"></span>HollowPine</div>
    <div class="brand__legal">HollowPine Ventures Inc.</div>
  </div>

  <div class="contact">
    <h1 class="contact__name">Will Marsh</h1>
    <p class="contact__title">President</p>
    <div class="contact__rule"></div>
    <ul class="contact__list">
      <li class="contact__item">
        <svg class="contact__icon" viewBox="0 0 24 24" aria-hidden="true"><path fill="var(--white)" d="M6.6 10.8a15.1 15.1 0 0 0 6.6 6.6l2.2-2.2a1 1 0 0 1 1-.25 11.4 11.4 0 0 0 3.6.57 1 1 0 0 1 1 1V20a1 1 0 0 1-1 1A17 17 0 0 1 3 4a1 1 0 0 1 1-1h3.5a1 1 0 0 1 1 1c0 1.25.2 2.45.57 3.57a1 1 0 0 1-.25 1z"/></svg>
        <span>555-214-3987</span>
      </li>
      <li class="contact__item">
        <svg class="contact__icon" viewBox="0 0 24 24" aria-hidden="true"><g fill="none" stroke="var(--white)" stroke-width="2"><circle cx="12" cy="12" r="9.5"/><ellipse cx="12" cy="12" rx="4" ry="9.5"/><path d="M2.5 12h19M4 7h16M4 17h16"/></g></svg>
        <span>hollowpineventures.example</span>
      </li>
      <li class="contact__item">
        <svg class="contact__icon" viewBox="0 0 24 24" aria-hidden="true"><rect x="2" y="5" width="20" height="14" fill="var(--white)"/><path d="M2.5 5.5 12 13l9.5-7.5" fill="none" stroke="var(--orange)" stroke-width="1.8"/></svg>
        <span>will@hollowpineventures.example</span>
      </li>
    </ul>
  </div>
</section>

<section class="card card--back" aria-label="Business card back">
  <svg class="card__shapes" viewBox="0 0 741 427" aria-hidden="true">
    <polygon points="55,427 80,397 240,397 215,427" fill="var(--navy)"/>
    <polygon points="380,427 405,397 741,397 741,427" fill="var(--orange)"/>
    <polygon points="741,360 741,397 712,397" fill="var(--orange)"/>
  </svg>

  <div class="brand">
    <div class="brand__name"><span class="brand__square"></span>HollowPine</div>
    <div class="brand__legal">HollowPine Ventures Inc.</div>
  </div>

  <ul class="services">
    <li class="services__item">Renovations</li>
    <li class="services__item">Additions</li>
    <li class="services__item">Repairs</li>
    <li class="services__item">New Home</li>
    <li class="services__item">Consultations</li>
  </ul>
</section>

</body>
</html>
```